Coporate Brochure

I want to create a 4-6 page brochure that presents our company , products and services to our clients. We want to focus on Products , service & repair

website is www.tqv-larchfield.com
line card also downloadable from website as well.

Target Market(s)

Industrial Plants and Water treatment plants

Industry/Entity Type

Industrial engineering

Requirements
Must have
• Stock images of pumps, motors, blowers and valves
Nice to have
• Nice stock photos

```html
<!DOCTYPE html>
<html lang="en">
<head>
<meta charset="utf-8">
<title>Liquid &amp; Dry Process Equipment – Brochure Cover</title>
<link rel="stylesheet" href="https://fonts.googleapis.com/css2?family=Archivo:wdth,wght@62..125,100..900&display=swap">
<style>
  :root {
    --brand-blue: #1f52a3;
    --brand-blue-deep: #173f86;
    --divider-grey: #c5c6c9;
    --paper: #ffffff;
    --ink: #111111;
    --ink-soft: #555555;
    --photo-orange: #f07a2c;
    --photo-glow: #ffd9a6;
    --photo-steel: #8fa0c4;
    --photo-navy: #1d2f73;
  }
  * { margin: 0; padding: 0; box-sizing: border-box; }
  html, body { width: 800px; height: 1200px; overflow: hidden; background: var(--paper); }
  .cover {
    position: relative;
    width: 800px;
    height: 1200px;
    overflow: hidden;
    font-family: "Archivo", Arial, sans-serif;
  }
  .cover-art { position: absolute; inset: 0; width: 800px; height: 1200px; }
  .cover-title {
    position: absolute;
    left: 0; right: 0;
    top: 560px;
    transform: translateY(-100%);
    text-align: center;
    color: var(--paper);
    font-weight: 900;
    font-stretch: 125%;
    font-size: 60px;
    line-height: 96px;
    letter-spacing: -1px;
    text-shadow: 3px 4px 6px rgba(0, 0, 0, 0.55);
    top: 446px;
  }
  .cover-title span { display: block; }
  .brand-name {
    position: absolute;
    left: 76px;
    top: 930px;
    display: flex;
    align-items: center;
    gap: 14px;
    color: var(--brand-blue);
    font-weight: 800;
    font-size: 40px;
    letter-spacing: -0.5px;
  }
  .brand-name .brand-dot {
    width: 22px; height: 22px;
    border-radius: 50%;
    background: var(--brand-blue);
  }
  .brand-message {
    position: absolute;
    left: 30px;
    width: 380px;
    top: 1068px;
    text-align: center;
    color: var(--ink-soft);
    font-size: 12.5px;
    line-height: 17px;
  }
  .brand-web {
    position: absolute;
    left: 30px;
    width: 380px;
    top: 1122px;
    text-align: center;
    color: var(--ink);
    font-weight: 600;
    font-size: 20px;
  }
  .contact {
    position: absolute;
    left: 557px;
    top: 1104px;
    color: var(--paper);
  }
  .contact-phone { font-size: 19px; font-weight: 500; line-height: 24px; }
  .contact-email { font-size: 15px; line-height: 20px; }
</style>
</head>
<body>
<main class="cover">
  <svg class="cover-art" viewBox="0 0 800 1200" aria-hidden="false">
    <defs>
      <radialGradient id="photo-tone" cx="0.36" cy="0.36" r="0.85">
        <stop offset="0" stop-color="var(--photo-glow)"/>
        <stop offset="0.18" stop-color="var(--photo-orange)"/>
        <stop offset="0.5" stop-color="var(--photo-steel)"/>
        <stop offset="1" stop-color="var(--photo-navy)"/>
      </radialGradient>
    </defs>
    <rect class="band-blue" x="0" y="0" width="800" height="1200" fill="var(--brand-blue)"/>
    <path class="cover-photo" role="img"
          aria-label="Photo of stainless steel process machinery with pipes and valves, lit by warm orange light with motion streaks"
          d="M0 0 H800 V666 C620 640 300 575 0 551 Z" fill="url(#photo-tone)"/>
    <path class="divider-grey"
          d="M0 596 L398 790 C470 826 518 900 503 990 C495 1060 465 1130 438 1200 L0 1200 Z"
          fill="var(--divider-grey)"/>
    <path class="panel-white"
          d="M0 618 L385 806 C455 842 495 912 484 992 C476 1060 448 1130 422 1200 L0 1200 Z"
          fill="var(--paper)"/>
  </svg>

  <h1 class="cover-title">
    <span>LIQUID &amp; DRY</span>
    <span>PROCESS</span>
    <span>EQUIPMENT</span>
  </h1>

  <div class="brand-name"><span class="brand-dot"></span>TQV Larchfield</div>

  <p class="brand-message">We appreciate every opportunity presented and look forward to becoming a valuable resource to your business.</p>
  <p class="brand-web">www.tqv-larchfield.com</p>

  <div class="contact">
    <p class="contact-phone">(555)014-2290</p>
    <p class="contact-email">sales@tqv-larchfield.com</p>
  </div>
</main>
</body>
</html>
```